Business card design needed

We need a business card for a new business. We are called Little Crew Wearhouse, and we make replica kid size clothing, mainly hi vis shirts, work trousers and shorts. Our long term goal is to include clothing for numerous trades and professions, for our littlest Aussies. We would like a kid friendly card using navy blue, bright orange, bright yellow and bright pink. We haven't set up our web page yet because we want to base it on our final business card design.
Updates

Industry/Entity Type

Clothing

```html
<!DOCTYPE html>
<html lang="en">
<head>
<meta charset="utf-8">
<title>Little Crew Wearhouse – Business Card</title>
<link rel="stylesheet" href="https://fonts.googleapis.com/css2?family=Arimo:wght@400;700&display=swap">
<style>
  :root {
    --navy: #2e3192;
    --orange: #f26f21;
    --yellow: #d7df23;
    --pink: #ec008c;
    --ink: #111111;
    --paper: #ffffff;
  }
  * { margin: 0; padding: 0; box-sizing: border-box; }
  html, body {
    width: 1200px;
    height: 692px;
    overflow: hidden;
    background: var(--paper);
  }
  .card {
    position: relative;
    width: 1200px;
    height: 692px;
    background: var(--paper);
    font-family: "Arimo", Arial, sans-serif;
    color: var(--ink);
  }
  .brand {
    position: absolute;
    left: 0;
    top: 196px;
    width: 1200px;
    height: 76px;
    display: flex;
    justify-content: center;
    align-items: center;
    gap: 26px;
  }
  .brand-square {
    width: 76px;
    height: 76px;
    background: var(--yellow);
    flex: none;
  }
  .brand-name {
    font-size: 66px;
    font-weight: 700;
    color: var(--pink);
    line-height: 1;
  }
  .details {
    position: absolute;
    left: 66px;
    top: 436px;
    font-size: 32px;
    line-height: 39.5px;
  }
  .details .person {
    font-weight: 700;
    color: var(--orange);
  }
  .phones {
    position: absolute;
    left: 560px;
    top: 436px;
    display: grid;
    grid-template-columns: 293px auto;
    column-gap: 59px;
    font-size: 32px;
    line-height: 39.5px;
    white-space: nowrap;
  }
  .phones .label {
    text-align: right;
    font-weight: 700;
  }
  .label.company { color: var(--pink); }
  .label.direct { color: var(--orange); }
  .label.cell { color: var(--navy); }
  .email {
    position: absolute;
    right: 64px;
    top: 594px;
    font-size: 32px;
    line-height: 39.5px;
    white-space: nowrap;
  }
</style>
</head>
<body>
  <div class="card">
    <div class="brand">
      <span class="brand-square"></span>
      <span class="brand-name">Little Crew Wearhouse</span>
    </div>

    <div class="details">
      <div class="person">Name</div>
      <div class="person">Job Title</div>
      <div>Little Crew Lane</div>
      <div>Harbourton NSW 2000</div>
      <div>littlecrewwearhouse.com.au</div>
    </div>

    <div class="phones">
      <span class="label company">COMPANY</span><span class="number">(99) 9999 9999</span>
      <span class="label direct">DIRECT</span><span class="number">(99) 9999 9999</span>
      <span class="label cell">CELL</span><span class="number">(99) 9999 9999</span>
    </div>

    <div class="email">name@littlecrewwearhouse.com.au</div>
  </div>
</body>
</html>
```